I need a better looking dashboard for my web application

I have a very table heavy web page that I would like to add a design touch to it. I have the logo and primary colors picked out, I just need some help in adding visual appeal the page. I would also like to add a couple of button to the page as shortcuts. Every spot that has a + sign could have a button added. I would also like to add another graph (the data will be in the uploaded files. Please feel free to ask any questions :-)

```html
<!DOCTYPE html>
<html lang="en">
<head>
<meta charset="utf-8">
<title>ShiftCover Dashboard</title>
<link href="https://fonts.googleapis.com/css2?family=Roboto:wght@400;500;700&display=swap" rel="stylesheet">
<style>
:root{
  --brand:#5b3a9b;
  --brand-dark:#4a2f86;
  --link:#2aa7c9;
  --text:#222;
  --muted:#888;
  --bg:#efefef;
  --panel:#fff;
  --cell:#f3f3f3;
  --line:#e3e3e3;
  --red:#dc3545;
  --green:#2fa84f;
}
*{box-sizing:border-box;margin:0;padding:0}
html,body{width:1200px;height:676px;overflow:hidden}
body{font-family:"Roboto",sans-serif;background:var(--bg);color:var(--text);position:relative}
.topbar{position:absolute;left:0;top:0;width:1200px;height:50px;background:#fff;border-bottom:1px solid #ddd;display:flex;align-items:center}
.brand{width:188px;height:50px;display:flex;align-items:center;padding-left:16px;gap:6px;border-right:1px solid var(--line);color:var(--brand);font-weight:700;font-size:20px}
.brand-mark{width:14px;height:14px;border-radius:50%;background:var(--brand)}
.nav{display:flex;align-items:center;gap:26px;padding-left:10px;font-size:11.5px;color:#777}
.nav-item{display:flex;align-items:center;gap:6px}
.nav-item.active{color:var(--brand);font-weight:500}
.nav svg{width:15px;height:15px;stroke:currentColor;fill:none;stroke-width:1.6}
.user{position:absolute;right:0;top:0;height:50px;display:flex;align-items:center;font-size:11.5px;color:#666}
.user .avatar{width:30px;height:30px;border-radius:50%;background:#8a6a55;margin:0 10px 0 6px}
.icon-cell{width:50px;height:50px;border-left:1px solid var(--line);display:flex;align-items:center;justify-content:center;color:#999}
.icon-cell svg{width:16px;height:16px;stroke:currentColor;fill:none;stroke-width:1.5}
.panel{position:absolute;background:var(--panel);border-radius:12px;overflow:hidden}
.panel-head{height:36px;display:flex;align-items:center;padding:0 15px}
.panel-title{font-size:11.5px;font-weight:500;flex:1}
.filter{width:126px;height:17px;border:1px solid var(--line);border-radius:9px;font-size:8.5px;color:#aaa;padding-left:9px;line-height:15px;margin-right:15px}
.btn{width:16px;height:16px;border-radius:3px;background:var(--brand);margin-left:6px;display:flex;align-items:center;justify-content:center}
.btn svg{width:10px;height:10px;stroke:#fff;fill:none;stroke-width:2}
table{border-collapse:separate;border-spacing:1px 3px;font-size:7.8px;margin-left:18px;table-layout:fixed}
th{font-weight:500;font-size:9px;height:22px;text-align:center;border-right:1px solid var(--line)}
td{background:var(--cell);height:21.5px;padding:0 6px;white-space:nowrap;overflow:hidden}
td.c{text-align:center}
.lnk{color:var(--link)}
.ic{display:inline-flex;gap:11px;color:#555}
.ic svg{width:8px;height:8px;stroke:currentColor;fill:none;stroke-width:1.6}
.mini{display:inline-block;width:15px;height:15px;border-radius:3px;vertical-align:middle;margin-right:4px}
.pp td{height:40px;font-size:9px;background:var(--cell)}
.pimg{width:30px;height:32px;border-radius:3px;margin:auto}
.opt{display:flex;gap:7px;justify-content:center}
.opt span{width:12px;height:12px;border-radius:2px;display:flex;align-items:center;justify-content:center}
.opt svg{width:8px;height:8px;stroke:#fff;fill:none;stroke-width:2.2}
.footer{position:absolute;left:0;top:638px;width:1200px;height:38px;background:#fff;border-top:1px solid #ddd;text-align:center;font-size:8.5px;color:#777;line-height:36px}
</style>
</head>
<body>

<header class="topbar">
  <div class="brand"><span class="brand-mark"></span>ShiftCover</div>
  <nav class="nav">
    <span class="nav-item active"><svg viewBox="0 0 16 16"><path d="M2 8l6-5 6 5v6H2z"/></svg>Home</span>
    <span class="nav-item"><svg viewBox="0 0 16 16"><path d="M8 1c1 3 4 5 4 9a4 4 0 01-8 0c0-2 1-3 2-4 0 2 1 3 2 3"/></svg>Demo Outbox</span>
    <span class="nav-item"><svg viewBox="0 0 16 16"><path d="M8 15s5-5 5-9a5 5 0 00-10 0c0 4 5 9 5 9z"/><circle cx="8" cy="6" r="2"/></svg>Location Admin ▾</span>
    <span class="nav-item"><svg viewBox="0 0 16 16"><path d="M5 1l3 5H2z"/><rect x="2" y="9" width="5" height="5"/><circle cx="11.5" cy="11.5" r="2.5"/></svg>Regular Staff ▾</span>
  </nav>
  <div class="user">dn.manager@example.com<span class="avatar" role="img" aria-label="User profile photo"></span>
    <span class="icon-cell"><svg viewBox="0 0 16 16"><path d="M4 11V7a4 4 0 018 0v4l1 1H3zM7 14h2"/></svg></span>
    <span class="icon-cell"><svg viewBox="0 0 16 16"><circle cx="8" cy="8" r="2.5"/><circle cx="8" cy="8" r="6"/></svg></span>
  </div>
</header>

<!-- Managed Openings -->
<section class="panel" style="left:20px;top:69px;width:568px;height:249px">
  <div class="panel-head"><div class="panel-title">Managed Openings</div><div class="filter">Enter Filter Keywords..</div>
    <span class="btn"><svg viewBox="0 0 10 10"><path d="M5 1v8M1 5h8"/></svg></span><span class="btn"><svg viewBox="0 0 10 10"><path d="M8 4a3 3 0 10 0 2M8 1v3H5"/></svg></span></div>
  <table>
    <colgroup><col style="width:47px"><col style="width:72px"><col style="width:92px"><col style="width:54px"><col style="width:101px"><col style="width:56px"><col style="width:109px"></colgroup>
    <tr><th style="border:0"></th><th>Category</th><th>Regular Staff</th><th>Status</th><th>Summary</th><th>Location</th><th style="border:0">Time Slots Summary</th></tr>
    <tr><td class="c"><span class="ic"><svg viewBox="0 0 8 8"><path d="M1 7l1-3 4-3 1 1-3 4z"/></svg><svg viewBox="0 0 8 8"><path d="M1 2h6M2 2v5h4V2M3 1h2"/></svg></span></td><td class="lnk">Food Service</td><td>Extra duty</td><td class="lnk">Assigned</td><td>Immediate Need! Library</td><td class="lnk">LJE</td><td>12/30 - 01/01 (2h 10m)</td></tr>
    <tr><td class="c"><span class="ic"><svg viewBox="0 0 8 8"><path d="M1 7l1-3 4-3 1 1-3 4z"/></svg><svg viewBox="0 0 8 8"><path d="M1 2h6M2 2v5h4V2M3 1h2"/></svg></span></td><td class="lnk">Teacher</td><td>Naoimi Willis</td><td class="lnk">Available</td><td>Immediate Need! Library</td><td class="lnk">LJE</td><td>12/30 - 01/01 (2h 10m)</td></tr>
    <tr><td class="c"><span class="ic"><svg viewBox="0 0 8 8"><path d="M1 7l1-3 4-3 1 1-3 4z"/></svg><svg viewBox="0 0 8 8"><path d="M1 2h6M2 2v5h4V2M3 1h2"/></svg></span></td><td class="lnk">Bus Driver</td><td>Extra duty</td><td class="lnk">Available</td><td>Immediate Need! Library</td><td class="lnk">LJE</td><td>12/30 - 01/01 (2h 10m)</td></tr>
    <tr><td class="c"><span class="ic"><svg viewBox="0 0 8 8"><path d="M1 7l1-3 4-3 1 1-3 4z"/></svg><svg viewBox="0 0 8 8"><path d="M1 2h6M2 2v5h4V2M3 1h2"/></svg></span></td><td class="lnk">Custodian</td><td>Extra duty</td><td class="lnk">Available</td><td>Immediate Need! Library</td><td class="lnk">LJE</td><td>12/30 - 01/01 (2h 10m)</td></tr>
    <tr><td class="c"><span class="ic"><svg viewBox="0 0 8 8"><path d="M1 7l1-3 4-3 1 1-3 4z"/></svg><svg viewBox="0 0 8 8"><path d="M1 2h6M2 2v5h4V2M3 1h2"/></svg></span></td><td class="lnk">Teacher's Aide</td><td>Extra duty</td><td class="lnk">Available</td><td>Immediate Need! Library</td><td class="lnk">LJE</td><td>12/30 - 01/01 (2h 10m)</td></tr>
    <tr><td class="c"><span class="ic"><svg viewBox="0 0 8 8"><path d="M1 7l1-3 4-3 1 1-3 4z"/></svg><svg viewBox="0 0 8 8"><path d="M1 2h6M2 2v5h4V2M3 1h2"/></svg></span></td><td class="lnk">Food Service</td><td>Gladys Richardson</td><td class="lnk">Available</td><td>Immediate Need! Library</td><td class="lnk">LJE</td><td>12/30 - 01/01 (2h 10m)</td></tr>
    <tr><td class="c"><span class="ic"><svg viewBox="0 0 8 8"><path d="M1 7l1-3 4-3 1 1-3 4z"/></svg><svg viewBox="0 0 8 8"><path d="M1 2h6M2 2v5h4V2M3 1h2"/></svg></span></td><td class="lnk">Teacher's Aide</td><td>Alan Bowman</td><td class="lnk">Available</td><td>Immediate Need! Library</td><td class="lnk">LJE</td><td>12/30 - 01/01 (2h 10m)</td></tr>
  </table>
</section>

<!-- Location Overview -->
<section class="panel" style="left:611px;top:69px;width:567px;height:249px">
  <div class="panel-head"><div class="panel-title">Location Overview</div></div>
  <svg style="position:absolute;left:0;top:0" width="567" height="249" viewBox="0 0 909 398" font-family="Roboto, sans-serif">
    <g font-size="9" fill="#222">
      <rect x="500" y="67" width="9" height="9" fill="#5b3a9b"/><text x="515" y="76">Opening : Unfilled</text>
      <rect x="638" y="67" width="9" height="9" fill="#2fa84f"/><text x="654" y="76">Opening : filled</text>
      <rect x="743" y="67" width="9" height="9" fill="#dc3545"/><text x="760" y="76">LeaveRequest : Pending</text>
    </g>
    <g stroke="#e5e5e5" stroke-width="1">
      <line x1="53" y1="102" x2="870" y2="102"/><line x1="53" y1="142" x2="870" y2="142"/><line x1="53" y1="182" x2="870" y2="182"/>
      <line x1="53" y1="222" x2="870" y2="222"/><line x1="53" y1="262" x2="870" y2="262"/><line x1="53" y1="302" x2="870" y2="302"/>
    </g>
    <line x1="53" y1="72" x2="53" y2="343" stroke="#222" stroke-width="1.5"/>
    <line x1="53" y1="342" x2="870" y2="342" stroke="#222" stroke-width="1.5"/>
    <g font-size="10" fill="#222" text-anchor="end">
      <text x="40" y="105">12</text><text x="40" y="145">10</text><text x="40" y="185">8</text><text x="40" y="225">6</text>
      <text x="40" y="265">4</text><text x="40" y="305">2</text><text x="40" y="345">0</text>
    </g>
    <rect x="104" y="282" width="30" height="60" fill="#5b3a9b"/><rect x="104" y="262" width="30" height="20" fill="#2fa84f"/>
    <rect x="146" y="262" width="29" height="80" fill="#dc3545"/>
    <rect x="275" y="242" width="30" height="100" fill="#5b3a9b"/><rect x="316" y="262" width="29" height="80" fill="#dc3545"/>
    <rect x="445" y="222" width="30" height="120" fill="#5b3a9b"/><rect x="486" y="142" width="29" height="200" fill="#dc3545"/>
    <rect x="616" y="242" width="29" height="100" fill="#5b3a9b"/><rect x="656" y="262" width="29" height="80" fill="#dc3545"/>
    <g font-size="9.5" fill="#222" text-anchor="middle">
      <text x="140" y="359">Lake Jonas Elementary</text><text x="310" y="360">Feestberg Middle School</text>
      <text x="481" y="360">West Devante Middle School</text><text x="651" y="362">East Devante Middle School</text>
    </g>
    <text x="454" y="384" font-size="13" font-weight="500" text-anchor="middle" fill="#222">LeaveRequest/Openings/Assignments</text>
  </svg>
</section>

<!-- Regular Staff Leave Request -->
<section class="panel" style="left:20px;top:337px;width:568px;height:250px">
  <div class="panel-head"><div class="panel-title">Regular Staff Leave Request</div><div class="filter">Enter Filter Keywords..</div>
    <span class="btn"><svg viewBox="0 0 10 10"><path d="M5 1v8M1 5h8"/></svg></span><span class="btn"><svg viewBox="0 0 10 10"><path d="M8 4a3 3 0 10 0 2M8 1v3H5"/></svg></span></div>
  <table>
    <colgroup><col style="width:47px"><col style="width:72px"><col style="width:131px"><col style="width:69px"><col style="width:100px"><col style="width:109px"></colgroup>
    <tr><th style="border:0"></th><th>Status</th><th>Full Name</th><th colspan="2">Openings</th><th style="border:0">Time Slots Summary</th></tr>
    <tr><th style="border:0;height:16px"></th><th style="height:16px"></th><th style="height:16px"></th><th style="height:16px">Assignments</th><th style="height:16px">Prearranged Sub</th><th style="border:0;height:16px"></th></tr>
    <tr><td class="c"><span class="ic"><svg viewBox="0 0 8 8"><path d="M1 7l1-3 4-3 1 1-3 4z"/></svg><svg viewBox="0 0 8 8"><path d="M0 4q4-4 8 0q-4 4-8 0z"/><circle cx="4" cy="4" r="1"/></svg></span></td><td>Pending</td><td class="lnk"><span class="mini" style="background:#9a7a6a" role="img" aria-label="Staff photo"></span>Naoimi Willis</td><td>N/A</td><td class="lnk">N/A</td><td>12/30 - 01/01 (2h 10m)</td></tr>
    <tr><td class="c"><span class="ic"><svg viewBox="0 0 8 8"><path d="M1 7l1-3 4-3 1 1-3 4z"/></svg><svg viewBox="0 0 8 8"><path d="M0 4q4-4 8 0q-4 4-8 0z"/><circle cx="4" cy="4" r="1"/></svg></span></td><td>Pending</td><td class="lnk"><span class="mini" style="background:#c9bdb5" role="img" aria-label="Staff photo"></span>Jeremy Gardner</td><td>N/A</td><td class="lnk">N/A</td><td>12/30 - 01/01 (2h 10m)</td></tr>
    <tr><td class="c"><span class="ic"><svg viewBox="0 0 8 8"><path d="M1 7l1-3 4-3 1 1-3 4z"/></svg><svg viewBox="0 0 8 8"><path d="M0 4q4-4 8 0q-4 4-8 0z"/><circle cx="4" cy="4" r="1"/></svg></span></td><td>Pending</td><td class="lnk"><span class="mini" style="background:#d8ccc2" role="img" aria-label="Staff photo"></span>Scarlett Cook</td><td>Counselor</td><td class="lnk">N/A</td><td>12/30 - 01/01 (2h 10m)</td></tr>
    <tr><td class="c"><span class="ic"><svg viewBox="0 0 8 8"><path d="M1 7l1-3 4-3 1 1-3 4z"/></svg><svg viewBox="0 0 8 8"><path d="M0 4q4-4 8 0q-4 4-8 0z"/><circle cx="4" cy="4" r="1"/></svg></span></td><td>Pending</td><td class="lnk"><span class="mini" style="background:#8f6b58" role="img" aria-label="Staff photo"></span>Hannah Collins</td><td>N/A</td><td class="lnk">N/A</td><td>12/30 - 01/01 (2h 10m)</td></tr>
    <tr><td class="c"><span class="ic"><svg viewBox="0 0 8 8"><path d="M1 7l1-3 4-3 1 1-3 4z"/></svg><svg viewBox="0 0 8 8"><path d="M0 4q4-4 8 0q-4 4-8 0z"/><circle cx="4" cy="4" r="1"/></svg></span></td><td>Pending</td><td class="lnk"><span class="mini" style="background:#7d8a90" role="img" aria-label="Staff photo"></span>Gladys Richardson</td><td>Administrator</td><td class="lnk"><span class="mini" style="background:#6f7a80" role="img" aria-label="Substitute photo"></span>Ian Robertson</td><td>12/30 - 01/01 (2h 10m)</td></tr>
    <tr><td class="c"><span class="ic"><svg viewBox="0 0 8 8"><path d="M1 7l1-3 4-3 1 1-3 4z"/></svg><svg viewBox="0 0 8 8"><path d="M0 4q4-4 8 0q-4 4-8 0z"/><circle cx="4" cy="4" r="1"/></svg></span></td><td>Pending</td><td class="lnk"><span class="mini" style="background:#6e6258" role="img" aria-label="Staff photo"></span>Alan Bowman</td><td>Administrator</td><td class="lnk">N/A</td><td>12/30 - 01/01 (2h 10m)</td></tr>
  </table>
</section>

<!-- Pending Profile Images -->
<section class="panel" style="left:611px;top:337px;width:567px;height:250px">
  <div class="panel-head"><div class="panel-title">Pending Profile Images</div><div class="filter">Enter Filter Keywords..</div>
    <span class="btn"><svg viewBox="0 0 10 10"><path d="M5 1v8M1 5h8"/></svg></span><span class="btn"><svg viewBox="0 0 10 10"><path d="M8 4a3 3 0 10 0 2M8 1v3H5"/></svg></span></div>
  <table style="margin-left:16px">
    <colgroup><col style="width:119px"><col style="width:131px"><col style="width:43px"><col style="width:149px"><col style="width:86px"></colgroup>
    <tr><th>Last Name</th><th>First Name</th><th colspan="2">Profile Images</th><th style="border:0">Options</th></tr>
    <tr><th style="height:16px"></th><th style="height:16px"></th><th style="height:16px">Pending</th><th style="height:16px">Prearranged Sub</th><th style="border:0;height:16px"></th></tr>
    <tr class="pp"><td style="padding-left:9px">Walters</td><td class="lnk" style="padding-left:9px">Kim</td><td><div class="pimg" style="background:#cbb8a8" role="img" aria-label="Pending profile photo"></div></td><td>None Available</td><td><div class="opt"><span style="background:var(--green)"><svg viewBox="0 0 8 8"><path d="M1 4l2 2 4-4"/></svg></span><span style="background:var(--red)"><svg viewBox="0 0 8 8"><path d="M1 1l6 6M7 1l-6 6"/></svg></span></div></td></tr>
    <tr class="pp"><td style="padding-left:9px">Stevens</td><td class="lnk" style="padding-left:9px">Masons</td><td><div class="pimg" style="background:#c49b80" role="img" aria-label="Pending profile photo"></div></td><td>None Available</td><td><div class="opt"><span style="background:var(--green)"><svg viewBox="0 0 8 8"><path d="M1 4l2 2 4-4"/></svg></span><span style="background:var(--red)"><svg viewBox="0 0 8 8"><path d="M1 1l6 6M7 1l-6 6"/></svg></span></div></td></tr>
    <tr class="pp"><td style="padding-left:9px">Morales</td><td class="lnk" style="padding-left:9px">Junes</td><td><div class="pimg" style="background:#8c6250" role="img" aria-label="Pending profile photo"></div></td><td>None Available</td><td><div class="opt"><span style="background:var(--green)"><svg viewBox="0 0 8 8"><path d="M1 4l2 2 4-4"/></svg></span><span style="background:var(--red)"><svg viewBox="0 0 8 8"><path d="M1 1l6 6M7 1l-6 6"/></svg></span></div></td></tr>
    <tr class="pp"><td style="padding-left:9px">Stephens</td><td class="lnk" style="padding-left:9px">Priscilla</td><td><div class="pimg" style="background:#5a4238" role="img" aria-label="Pending profile photo"></div></td><td>None Available</td><td><div class="opt"><span style="background:var(--green)"><svg viewBox="0 0 8 8"><path d="M1 4l2 2 4-4"/></svg></span><span style="background:var(--red)"><svg viewBox="0 0 8 8"><path d="M1 1l6 6M7 1l-6 6"/></svg></span></div></td></tr>
  </table>
</section>

<!-- Bottom panels -->
<section class="panel" style="left:20px;top:606px;width:568px;height:50px">
  <div class="panel-head"><div class="panel-title">My Leave Requests</div><div class="filter">Enter Filter Keywords..</div>
    <span class="btn"><svg viewBox="0 0 10 10"><path d="M5 1v8M1 5h8"/></svg></span><span class="btn"><svg viewBox="0 0 10 10"><path d="M8 4a3 3 0 10 0 2M8 1v3H5"/></svg></span></div>
</section>
<section class="panel" style="left:611px;top:606px;width:567px;height:50px">
  <div class="panel-head"><div class="panel-title">Substitute Attendance</div><div class="filter">Enter Filter Keywords..</div>
    <span class="btn"><svg viewBox="0 0 10 10"><path d="M5 1v8M1 5h8"/></svg></span><span class="btn"><svg viewBox="0 0 10 10"><path d="M8 4a3 3 0 10 0 2M8 1v3H5"/></svg></span></div>
</section>

<footer class="footer">Copyright Northbay Systems. All Rights Reserved. (v0.8.4)</footer>
</body>
</html>
```